cleaning service

we are a cleaning company,

we have a current flyer but its very dull

I have attached it, can we make it look modern, maybe add pictures and colour

```html
<!DOCTYPE html>
<html lang="en">
<head>
<meta charset="utf-8">
<title>Marla's Cleaning Service – Brochure</title>
<link href="https://fonts.googleapis.com/css2?family=Montserrat:wght@600;700;800&family=Open+Sans:wght@400;600&display=swap" rel="stylesheet">
<style>
:root{
  --bg:#2b2b2b;
  --paper:#ffffff;
  --teal:#1596a8;
  --teal-dark:#0e6f7e;
  --green:#7dbb3b;
  --ink:#3a3a3a;
  --muted:#6b6b6b;
  --red:#d6262c;
  --row:#e8f4f6;
  --photo-a:#b9d7de;
  --photo-b:#e8c7a8;
}
*{margin:0;padding:0;box-sizing:border-box}
html,body{width:841px;height:1200px;overflow:hidden;background:var(--bg)}
body{position:relative;font-family:"Open Sans",Arial,sans-serif;color:var(--ink)}
.sheet{position:absolute;left:12px;width:817px;background:var(--paper);display:flex;box-shadow:0 4px 14px rgba(0,0,0,.5)}
.sheet--outside{top:22px;height:540px}
.sheet--inside{top:612px;height:566px}
.panel{position:relative;width:272.3px;height:100%;padding:16px 16px;border-right:1px dashed #e2e2e2;overflow:hidden}
.panel:last-child{border-right:none}
h3{font-family:"Montserrat",Arial,sans-serif;font-weight:700;font-size:11px;color:var(--teal);margin:6px 0 4px}
p{font-size:6.2px;line-height:1.5;margin-bottom:5px;color:var(--muted)}
.price{width:100%;border-collapse:collapse;margin:4px 0 8px;font-size:6px}
.price th{background:var(--teal);color:#fff;text-align:left;padding:2px 4px;font-weight:600}
.price td{padding:2px 4px;border-bottom:1px solid #fff}
.price tr:nth-child(even) td{background:var(--row)}
.photo{display:block;width:100%;background:linear-gradient(135deg,var(--photo-a),var(--photo-b))}
.brand{display:flex;align-items:center;gap:7px}
.brand__dot{width:22px;height:22px;border-radius:50%;background:var(--teal)}
.brand__name{font-family:"Montserrat",Arial,sans-serif;font-weight:800;font-size:15px;color:var(--teal);line-height:1}
.center{text-align:center}
.contact{font-size:7px;line-height:1.7;color:var(--ink);margin-top:10px}
.band{background:var(--green);color:#fff;font-family:"Montserrat",Arial,sans-serif;font-weight:800;text-align:right;padding:12px 16px;font-size:17px;line-height:1.15;margin:0 -16px}
.tagline{font-family:"Montserrat",Arial,sans-serif;font-size:6.5px;letter-spacing:2px;color:var(--teal);text-align:right;margin-top:8px}
.web{position:absolute;left:0;right:0;bottom:0;background:var(--teal);color:#fff;font-family:"Montserrat",Arial,sans-serif;font-weight:700;font-size:11px;text-align:center;padding:10px 0}
.offer{position:absolute;left:70px;bottom:64px;width:90px;height:90px;border-radius:50%;background:var(--red);color:#fff;text-align:center;font-family:"Montserrat",Arial,sans-serif;padding-top:20px;border:3px solid #fff;box-shadow:0 0 0 2px var(--red)}
.offer b{display:block;font-size:24px;line-height:1}
.offer span{font-size:8px;font-weight:700;letter-spacing:1px}
.offer-note{position:absolute;left:16px;right:16px;bottom:34px;text-align:center;font-size:6.5px;font-weight:600;color:var(--red)}
</style>
</head>
<body>

<section class="sheet sheet--outside">
  <div class="panel">
    <h3>Upholstery Cleaning</h3>
    <p>Keeping your furniture fresh is vital for a healthy home. We use gentle steam and safe products that lift deep dirt, pet hair and stains from sofas, chairs and cushions without harm to fabric.</p>
    <table class="price">
      <tr><th>Item</th><th>Price</th></tr>
      <tr><td>Armchair</td><td>$45</td></tr>
      <tr><td>Loveseat</td><td>$75</td></tr>
      <tr><td>Three seat sofa</td><td>$95</td></tr>
      <tr><td>Sectional</td><td>$140</td></tr>
    </table>
    <p>All prices include pre treatment and deodorising. Extra charges may apply for heavily soiled pieces.</p>
    <p>Our upholstery cleaning team is trained to work with every fabric type, from cotton and linen to leather and microfibre. We test each piece first so colours stay bright and fibres stay soft after every clean.</p>
    <h3>Mattress Cleaning</h3>
    <p>Mattresses collect dust mites, sweat and allergens over time. Our deep extraction method removes hidden dirt and odours, leaving your bed fresh and hygienic. Ideal for families with children, pets or allergies. Most mattresses are dry within a few hours.</p>
    <p>We also apply an optional protective treatment to keep stains from setting in.</p>
    <h3>Curtain Cleaning</h3>
    <p>Curtains and drapes trap dust, smoke and cooking smells. We clean them on site without taking them down, saving you time and effort. Our low moisture process is safe for delicate fabrics and leaves them fresh, bright and ready to enjoy again.</p>
    <p>Ask about blinds and sheer cleaning when you book your visit.</p>
  </div>

  <div class="panel center">
    <div style="margin-top:150px" class="brand" aria-label="Marla's Cleaning Service">
      <span class="brand__dot"></span><span class="brand__name">MARLA'S<br><span style="font-size:8px;font-weight:700">CLEANING SERVICE</span></span>
    </div>
    <div class="contact">
      125 Harbour Meadows Rd.<br>
      Lakeview, ON L2X 4P8<br>
      (555) 014-2290<br>
      hello@marlascleaning.example
    </div>
    <p style="margin-top:16px">Locally owned and fully insured. We bring our own eco friendly supplies and equipment to every home and office we serve.</p>
  </div>

  <div class="panel" style="padding-top:0">
    <div class="photo" style="height:200px;margin:0 -16px" role="img" aria-label="Smiling cleaner in gloves wiping a kitchen counter"></div>
    <div class="brand" style="justify-content:flex-end;margin:14px 0 14px">
      <span class="brand__dot"></span><span class="brand__name">MARLA'S<br><span style="font-size:8px;font-weight:700">CLEANING SERVICE</span></span>
    </div>
    <div class="band">TAKE BACK YOUR<br>TIME BY LEAVING THE<br>CLEANING TO US.</div>
    <div class="tagline">RESIDENTIAL · COMMERCIAL · HOLIDAYS</div>
    <div class="web">WWW.MARLASCLEANING.EXAMPLE</div>
  </div>
</section>

<section class="sheet sheet--inside">
  <div class="panel" style="padding-top:0">
    <div class="photo" style="height:170px;margin:0 -16px 10px" role="img" aria-label="Two cleaners in uniform dusting a bright living room"></div>
    <p>Marla's Cleaning Service offers professional cleaning services to homes and businesses across the region. From weekly tidies to one off deep cleans, our friendly team arrives on time and leaves every room spotless.</p>
    <p>All our cleaners are carefully screened and trained in safe methods that protect your family, pets and property. We listen to your needs and build a plan that suits your schedule and budget.</p>
    <p>Whether it is a busy family home or a small office, we handle dusting, vacuuming, mopping, bathrooms and kitchens with care. Your satisfaction is always guaranteed.</p>
    <div class="offer"><span>SPECIAL</span><b>20%</b><span>OFFER</span></div>
    <div class="offer-note">Please call us on (555) 014-2290 to book your service</div>
  </div>

  <div class="panel">
    <h3>Antiviral Sanitisation Service</h3>
    <p>Our sanitising treatment uses hospital grade disinfectants approved for household use. We target high touch areas such as handles, switches, railings and counters to reduce germs and keep your space safe.</p>
    <p>The service is ideal for homes, offices, shops and rental units. We use fogging equipment and wipe down methods that reach every surface, leaving no harsh residue behind. Treatments can be booked on their own or added to any regular clean.</p>
    <p>All products are safe for children and pets once dry, and our team wears full protective gear during each visit.</p>
    <h3>Our Off Lease Cleaning Service</h3>
    <p>Moving out can be stressful. Our end of lease clean covers every room from top to bottom so you can hand back the keys with confidence. We follow a detailed checklist built around common landlord requirements.</p>
    <table class="price">
      <tr><th>Property</th><th>Price</th></tr>
      <tr><td>Studio / 1 bedroom</td><td>$220</td></tr>
      <tr><td>2 bedroom</td><td>$290</td></tr>
      <tr><td>3 bedroom</td><td>$360</td></tr>
      <tr><td>4 bedroom +</td><td>$430</td></tr>
    </table>
    <p>Includes inside cupboards, appliances, windows, skirting boards and floors. If anything is missed, we return to fix it at no extra cost.</p>
  </div>

  <div class="panel">
    <h3>Carpet Cleaning</h3>
    <p>Regular carpet cleaning extends the life of your flooring and improves indoor air. Our hot water extraction removes deep dirt, allergens and stains, and carpets dry quickly so you can get back to normal fast.</p>
    <table class="price">
      <tr><th>Area</th><th>Price</th></tr>
      <tr><td>Single bedroom</td><td>$35</td></tr>
      <tr><td>Living room</td><td>$50</td></tr>
      <tr><td>Hallway</td><td>$25</td></tr>
      <tr><td>Staircase</td><td>$60</td></tr>
      <tr><td>Whole home</td><td>$180</td></tr>
    </table>
    <h3>Rug Cleaning</h3>
    <p>From wool to synthetic, we clean rugs gently and thoroughly. Colours are tested first, then each rug is washed, rinsed and groomed to restore its softness and shine.</p>
    <div class="photo" style="height:110px;margin:6px 0 6px" role="img" aria-label="Cleaner vacuuming a patterned rug"></div>
    <h3>Oven Cleaning</h3>
    <p>Baked on grease and carbon are no match for our oven team. We strip racks, trays and doors, soak them in safe solutions and leave your oven looking like new, inside and out.</p>
  </div>
</section>

</body>
</html>
```